A billboard for Harlow Ridge Construction size 36.5’ x 14.5’

Hi guys. We are purchasing a billboard and are looking for a design (size 36.5’ x 14.5’). Our slogan is "Quality you deserve, service you can count on". The goal of this billboard is brand recognition primarily letting people know we do roofs. Attached are logos that can be used if needed. Not necessarily all of them need to be used.

Target Market(s)

Residents in the local areas needing or thinking about a roof replacement

Industry/Entity Type

Roofing

Requirements
Must have
• Logo and services (roof replacement, gutters, siding, and snow removal)
Nice to have
• take a look at our website for ideas www.harlowridgeconstruction.example

```html
<!DOCTYPE html>
<html lang="en">
<head>
<meta charset="utf-8">
<title>Harlow Ridge Construction Billboard</title>
<link rel="stylesheet" href="https://fonts.googleapis.com/css2?family=Montserrat:wght@700;800;900&family=Playfair+Display:wght@500&display=swap">
<style>
  :root {
    --red: #e8202f;
    --black: #0d0d0e;
    --white: #ffffff;
    --slate: #3a3b3d;
    --slate-dark: #2b2c2e;
    --badge: #5a5c62;
  }
  * { margin: 0; padding: 0; box-sizing: border-box; }
  html, body { width: 1200px; height: 477px; overflow: hidden; background: var(--white); }
  .billboard { position: relative; width: 1200px; height: 477px; overflow: hidden; background: var(--white); font-family: "Montserrat", sans-serif; }

  .contact-band { position: absolute; left: 0; top: 270px; width: 540px; height: 100px; background: var(--black); }

  .brand-name {
    position: absolute; left: 40px; top: 78px; width: 460px;
    font-family: "Playfair Display", serif; font-weight: 500;
    font-size: 50px; line-height: 1.05; color: var(--black); text-align: center;
  }

  .phone-box {
    position: absolute; left: 37px; top: 247px; width: 471px; height: 63px;
    background: var(--red); clip-path: polygon(4% 0, 100% 0, 96% 100%, 0 100%);
    display: flex; align-items: center; justify-content: center; gap: 14px;
  }
  .phone-icon { width: 40px; height: 40px; }
  .phone-number { color: var(--white); font-weight: 800; font-size: 44px; letter-spacing: 0.5px; }

  .website {
    position: absolute; left: 20px; top: 326px; width: 500px; text-align: center;
    color: var(--white); font-weight: 700; font-size: 17px; letter-spacing: 1.2px;
    font-variant: small-caps;
  }

  .house-photo {
    position: absolute; left: 0; top: 0; width: 1200px; height: 370px;
    background: linear-gradient(180deg, #8aa0bd 0%, #cfc6b4 22%, #6f7a78 45%, #9fb1ae 65%, #6b6a4e 100%);
    clip-path: polygon(582px 0, 920px 0, 853px 370px, 517px 370px);
  }

  .supplier { position: absolute; left: 950px; top: 90px; width: 140px; font-weight: 800; font-size: 24px; line-height: 1; color: var(--black); text-align: center; }
  .supplier-badge { position: absolute; left: 1097px; top: 93px; width: 38px; height: 65px; background: var(--badge); }

  .slogan { position: absolute; left: 890px; top: 204px; width: 290px; text-align: center; font-weight: 900; font-size: 29px; line-height: 31px; color: var(--black); }
  .slogan .accent { color: var(--red); }

  .divider { position: absolute; left: 0; top: 370px; width: 1200px; height: 7px; background: var(--red); }
  .services-band {
    position: absolute; left: 0; top: 377px; width: 1200px; height: 100px;
    background: linear-gradient(180deg, var(--slate) 0%, var(--slate-dark) 100%);
    display: flex; align-items: center; justify-content: center;
  }
  .services { color: var(--white); font-weight: 800; font-size: 28px; letter-spacing: 2px; white-space: nowrap; }
</style>
</head>
<body>
<main class="billboard">
  <div class="contact-band"></div>

  <h1 class="brand-name">Harlow Ridge<br>Construction</h1>

  <div class="phone-box">
    <svg class="phone-icon" viewBox="0 0 40 40" aria-hidden="true">
      <circle cx="20" cy="20" r="20" fill="#0d0d0e"/>
      <path d="M14.5 11c.6-.4 1.4-.3 1.8.3l2 3c.4.6.3 1.3-.2 1.8l-1.3 1.2c.8 1.9 2.4 3.6 4.3 4.5l1.3-1.3c.5-.5 1.2-.6 1.8-.2l3 2c.6.4.7 1.2.3 1.8l-1.2 1.8c-.6.9-1.7 1.3-2.8 1-5.2-1.4-9.4-5.6-10.8-10.8-.3-1.1.1-2.2 1-2.8z" fill="#ffffff"/>
    </svg>
    <span class="phone-number">555-018-2740</span>
  </div>

  <p class="website">www.harlowridgeconstruction.example</p>

  <div class="house-photo" role="img" aria-label="Photo of a two-storey sage green house with a grey shingled roof and white porch under a partly cloudy sky"></div>

  <p class="supplier">Summit Shingles</p>
  <div class="supplier-badge" aria-hidden="true"></div>

  <p class="slogan">QUALITY YOU<br>DESERVE,<br><span class="accent">SERVICE YOU<br>CAN COUNT ON</span></p>

  <div class="divider"></div>
  <div class="services-band">
    <p class="services">ROOF REPLACEMENT • GUTTERS • SIDING • SNOW REMOVAL</p>
  </div>
</main>
</body>
</html>
```